Commerical Office Furniture Company Needs Truck Wrap Design for Box Truck

We need a truck wrap design (and business card) for our company based in Fresno, California. We offer commercial office furnishings such as private office desks, cubicle stations, conference tables, all office seating (task chairs, guest, lobby/lounge, conference) storage systems, ergonomic solutions (monitor arms, keyboard trays, lift desks) and much more. We are a full service office furniture dealer who can fully outfit every space and need for a new or existing office space. We also offer design and space planning services and professional installation.
We would like our trap wrap to be modern using the same color scheme as our logo with a clean but eye catching look. Perhaps using a few nice looking desk/workstations product images as examples to show people what we are capable of. We attached some examples of some themes/layouts we like. feel free to be creative. Our website trymoldavo.com has some images and info.
https://photoshelf.brovane-co.com/detail/client-space-shared-tessel-workstation-with-q-line-storage-height-adjustable-tables-and-wexmoor-seating
Target Market(s)
Private Sector, Education, Healthcare
Industry/Entity Type
Requirements
Must have
- Dorvik Box Truck - 190 inches x 85 inches

```html
<!DOCTYPE html>
<html lang="en">
<head>
<meta charset="utf-8">
<title>Moldavo Office Interiors — Box Truck Wrap</title>
<link rel="stylesheet" href="https://fonts.googleapis.com/css2?family=Barlow+Semi+Condensed:wght@600;700;800&family=Montserrat:wght@800&family=Barlow:wght@800&display=swap">
<style>
  :root {
    --brand-blue: #1b4ee6;
    --panel-dark: #242428;
    --ink: #2e2e33;
    --ink-soft: #55555c;
    --white: #ffffff;
    --page: #0c0c0d;
    --reflect-red: #d8322c;
    --photo-dark: #4a463f;
    --photo-light: #b9b3a8;
  }
  * { box-sizing: border-box; margin: 0; padding: 0; }
  html, body { width: 705px; height: 1200px; overflow: hidden; background: var(--page); }
  body { position: relative; font-family: "Barlow Semi Condensed", sans-serif; }

  .panel { position: absolute; background: var(--white); overflow: hidden; border-radius: 4px; }

  /* Shared pieces */
  .photo-band { position: absolute; left: 0; top: 0; width: 100%; background: var(--panel-dark); }
  .photo-band::after { content: ""; position: absolute; left: 0; bottom: -5px; width: 100%; height: 5px; background: var(--brand-blue); }
  .product-photo { position: absolute; border: 2px solid var(--white);
    background: linear-gradient(180deg, var(--photo-light) 0%, #8d877c 45%, var(--photo-dark) 100%); }

  .name-mark { position: absolute; display: flex; align-items: center; gap: 10px;
    color: var(--brand-blue); font-weight: 800; line-height: 1; white-space: nowrap; }
  .name-mark .dot { background: var(--brand-blue); flex: none; }

  .descriptor { position: absolute; white-space: nowrap; }
  .descriptor .line { display: block; color: var(--ink); font-weight: 700; line-height: 1.05; }
  .descriptor .tagline { display: block; color: var(--ink-soft); font-weight: 600; line-height: 1; }

  .contact-band { position: absolute; left: 0; width: 100%; background: var(--brand-blue); }
  .website { color: var(--white); text-transform: uppercase; white-space: nowrap; }
  .phone-box { position: absolute; background: var(--panel-dark); color: var(--white); border-radius: 10px;
    font: 800 24px/1 "Barlow", sans-serif; display: flex; align-items: center; justify-content: center; }

  .reflective-strip { position: absolute; left: 0; width: 100%; height: 5px;
    background: repeating-linear-gradient(90deg, var(--reflect-red) 0 26px, var(--white) 26px 40px); }

  /* Side panel */
  .side-panel { left: 20px; top: 40px; width: 665px; height: 320px; }
  .side-panel .photo-band { height: 82px; }
  .side-panel .product-photo { top: 10px; width: 198px; height: 62px; }
  .side-panel .product-photo:nth-child(1) { left: 14px; }
  .side-panel .product-photo:nth-child(2) { left: 233px; }
  .side-panel .product-photo:nth-child(3) { left: 452px; }
  .side-panel .name-mark { left: 30px; top: 122px; font-size: 68px; }
  .side-panel .name-mark .dot { width: 18px; height: 18px; }
  .side-panel .descriptor { left: 336px; top: 120px; }
  .side-panel .descriptor .line { font-size: 38px; }
  .side-panel .descriptor .tagline { font-size: 17px; margin-top: 8px; }
  .side-panel .contact-band { top: 238px; height: 50px; }
  .side-panel .website { position: absolute; left: 26px; top: 15px; font: 800 20px/1 "Montserrat", sans-serif; letter-spacing: 5px; }
  .side-panel .phone-box { right: 16px; top: 4px; width: 222px; height: 42px; }
  .side-panel .reflective-strip { top: 298px; }

  /* Rear panel */
  .rear-panel { left: 20px; top: 400px; width: 330px; height: 380px; }
  .rear-header { position: absolute; left: 0; top: 0; width: 100%; height: 70px; background: var(--panel-dark); }
  .rear-header::after { content: ""; position: absolute; left: 0; bottom: -5px; width: 100%; height: 5px; background: var(--brand-blue); }
  .rear-header .website { display: block; width: 100%; text-align: center; font: 700 30px/70px "Barlow Semi Condensed", sans-serif; }
  .rear-panel .name-mark { left: 0; width: 100%; justify-content: center; top: 104px; font-size: 60px; }
  .rear-panel .name-mark .dot { width: 15px; height: 15px; }
  .rear-panel .descriptor { left: 0; width: 100%; text-align: center; top: 184px; }
  .rear-panel .descriptor .line { font-size: 30px; }
  .rear-panel .descriptor .tagline { font-size: 14px; margin-top: 7px; }
  .rear-panel .contact-band { top: 288px; height: 76px; }
  .rear-phone { position: absolute; width: 100%; text-align: center; top: 20px; color: var(--white); font: 800 36px/1 "Barlow", sans-serif; }
  .tail-light { position: absolute; top: 18px; width: 8px; height: 40px; border-radius: 4px; background: var(--reflect-red); }
  .tail-light.left { left: 8px; } .tail-light.right { right: 8px; }

  /* Cab door panel */
  .cab-panel { left: 375px; top: 400px; width: 310px; height: 380px; }
  .cab-panel .name-mark { left: 0; width: 100%; justify-content: center; top: 106px; font-size: 50px; }
  .cab-panel .name-mark .dot { width: 13px; height: 13px; }
  .cab-panel .descriptor { left: 0; width: 100%; text-align: center; top: 172px; }
  .cab-panel .descriptor .line { font-size: 26px; }
  .cab-panel .descriptor .tagline { font-size: 13px; margin-top: 6px; }
  .cab-lower { position: absolute; left: 0; bottom: 0; width: 100%; height: 100px; background: var(--brand-blue); }
  .cab-lower svg { position: absolute; left: 0; top: -28px; }
</style>
</head>
<body>

  <section class="panel side-panel">
    <div class="photo-band">
      <div class="product-photo" role="img" aria-label="Photo of an L-shaped executive desk in a private office"></div>
      <div class="product-photo" role="img" aria-label="Photo of a grey laminate desk with storage credenza"></div>
      <div class="product-photo" role="img" aria-label="Photo of shared workstations with glass panels"></div>
    </div>
    <div class="name-mark"><span class="dot"></span>MOLDAVO</div>
    <div class="descriptor">
      <span class="line">Office Interiors</span>
      <span class="tagline">Office Furniture&nbsp; • &nbsp;Design&nbsp; • &nbsp;Installation</span>
    </div>
    <div class="contact-band">
      <span class="website">trymoldavo.com</span>
      <span class="phone-box">(555) 014-7300</span>
    </div>
    <div class="reflective-strip"></div>
  </section>

  <section class="panel rear-panel">
    <div class="rear-header"><span class="website">trymoldavo.com</span></div>
    <div class="name-mark"><span class="dot"></span>MOLDAVO</div>
    <div class="descriptor">
      <span class="line">Office Interiors</span>
      <span class="tagline">Office Furniture • Design • Installation</span>
    </div>
    <div class="contact-band">
      <span class="tail-light left"></span>
      <span class="rear-phone">(555) 014-7300</span>
      <span class="tail-light right"></span>
    </div>
  </section>

  <section class="panel cab-panel">
    <div class="name-mark"><span class="dot"></span>MOLDAVO</div>
    <div class="descriptor">
      <span class="line">Office Interiors</span>
      <span class="tagline">Office Furniture • Design • Installation</span>
    </div>
    <div class="cab-lower">
      <svg width="310" height="30" viewBox="0 0 310 30" aria-hidden="true">
        <path d="M0 30 L0 22 C90 22 200 14 310 0 L310 30 Z" fill="var(--brand-blue)"/>
        <path d="M0 20 C90 20 200 12 310 -2" stroke="var(--panel-dark)" stroke-width="4" fill="none"/>
      </svg>
    </div>
  </section>

</body>
</html>
```